そよかぜ日記(http://www.soyokaze-nikki.com/)から発刊した、Lumora電子書籍の表紙のデザインをコンペ形式で募集いたします。 電子書籍「庭仕事の始め方: 3年で畑を百坪に広げた家庭菜園術」(http://www.shoppomart.jp/exec/tenpo/item/Q77KTX3MZA/) の表紙をリニューアルします。 ファイル形式はjpeg(1600×2560px) 50MB未満でお願いします。 .psdファイルも一緒に納品してください(.pdfも可能)。 白地または非常に薄い背景色の表紙画像は、白い背景との区別がつかなくなる場合があります。幅の狭い (3 ~ 4 ピクセル) 薄灰色の枠線を追加して、表紙の境界を明確にしてください。 現在の表紙デザインに沿う必要はありません。書籍の魅力・内容をしっかりアピールしてくれるデザインを選んで採用させていただきます。 ご不明点や質問はお気軽にご相談ご相談ください。 たくさんのデザイナーの皆様からのご連絡・ご提案をお待ちしております。 |
タイトルが目につきやすいことと、シンプルですが軽くない感じのデザインが気に入りました。
皆さま、多くのご提案ありがとうございました。色々なタイプのデザインを拝見させていただくことができました。これから出版する電子書籍については、コンペで作ってもらおうと考えています。これからもよろしくお願いします。

```html
<!DOCTYPE html>
<html lang="ja">
<head>
<meta charset="UTF-8">
<title>庭仕事の始め方 表紙</title>
<link rel="stylesheet" href="https://fonts.googleapis.com/css2?family=M+PLUS+1p:wght@800;900&display=swap">
<style>
  :root {
    --green: #3cb84a;
    --ink: #111111;
    --red: #e0241b;
    --white: #ffffff;
    --photo-dark: #2a2623;
    --photo-mid: #6d645b;
    --photo-light: #b9b2a8;
  }
  html, body {
    margin: 0;
    padding: 0;
    width: 749px;
    height: 1200px;
    overflow: hidden;
    background: var(--white);
  }
  .cover {
    position: relative;
    width: 749px;
    height: 1200px;
    overflow: hidden;
    font-family: "M PLUS 1p", sans-serif;
    background: var(--white);
  }
  .cover-photo {
    position: absolute;
    left: 0; top: 0;
    width: 749px;
    height: 868px;
    background:
      radial-gradient(ellipse at 40% 55%, #4a4a4c 0%, rgba(40,40,42,0) 45%),
      linear-gradient(160deg, var(--photo-dark) 0%, #3a342f 35%, var(--photo-mid) 70%, var(--photo-light) 100%);
  }
  .series-band {
    position: absolute;
    left: 0; top: 0;
    width: 749px;
    height: 122px;
    background: var(--green);
    color: var(--white);
    font-weight: 900;
    font-size: 70px;
    line-height: 122px;
    text-align: center;
    letter-spacing: 2px;
  }
  .subtitle {
    position: absolute;
    left: 27px; top: 148px;
    width: 696px;
    height: 80px;
    background: var(--white);
    color: var(--ink);
    font-weight: 900;
    font-size: 52px;
    line-height: 80px;
    text-align: center;
    letter-spacing: 1px;
  }
  .main-title {
    position: absolute;
    left: 40px; top: 250px;
    width: 669px;
    margin: 0;
    font-weight: 900;
    font-size: 172px;
    line-height: 185px;
    color: var(--white);
    -webkit-text-stroke: 10px var(--ink);
    paint-order: stroke fill;
  }
  .main-title .title-row {
    display: flex;
    justify-content: space-between;
  }
  .main-title .title-row.short {
    justify-content: space-around;
  }
  .blurb {
    position: absolute;
    left: 26px; top: 876px;
    width: 700px;
    margin: 0;
    font-weight: 900;
    font-size: 41px;
    line-height: 56px;
    color: var(--ink);
    letter-spacing: 0.5px;
    white-space: nowrap;
  }
  .blurb .accent { color: var(--red); }
  .author {
    position: absolute;
    right: 40px; top: 1126px;
    margin: 0;
    font-weight: 800;
    font-size: 37px;
    color: var(--ink);
  }
  .author .label { margin-right: 24px; }
</style>
</head>
<body>
  <div class="cover">
    <div class="cover-photo" role="img" aria-label="木のデスクの上でノートパソコンを操作する手元の写真"></div>

    <div class="series-band">庭仕事の始め方</div>
    <div class="subtitle">3年で畑を百坪に広げた</div>

    <h1 class="main-title">
      <span class="title-row short"><span>家</span><span>庭</span></span>
      <span class="title-row"><span>菜</span><span>園</span><span>術</span></span>
    </h1>

    <p class="blurb">
      <span class="accent">土づくりの基本</span>と<span class="accent">季節の感覚</span>を<br>
      頼りに、<span class="accent">たった3年で百坪</span>もの<br>
      畑を育て上げた<span class="accent">家庭菜園</span>の<br>
      実経験を<span class="accent">ノウハウ</span>にまとめました。
    </p>

    <p class="author"><span class="label">著者</span>そら吉</p>
  </div>
</body>
</html>
```